Stylish, Masculine Design - Men's Clothing

Granary Coat Mart is a 14,000 square foot warehouse outlet store open to the public since 2005. 50+ brands. Well-known designer brand names and private labels. 30-80% off retail everyday. Lowest prices guaranteed. Average suit price $150. Average shirt price $20. One-stop shop shopping. Men's suits, tuxedos, tuxedo rentals, dress shirts, ties, dress shoes, boy's suits and tuxedos, clergy robes, clergy shirts, cologne, loungewear. Slim fits (Prom Dance), business styles, "church" fashion, security-related uniform. Alterations done by expert tailors on premises for an extra charge.
The final design for both business card and logo should portray stylishness and masculinity.
Updates
We will be changing our name. Details below.New name: Warehouse Suit & TuxFormer name: Granary Coat Mart Added Monday, December 26, 2016
Target Market(s)
Gender: 80% Male, 15% Female, 5% Transgender
Location: 80% 10 Mile Radius, 20% >10 Mile Radius
Age: 17-18 (Primarily prom), 18-35 (Primarily Interviews and Weddings), 36-70 (primarily Church and events)
Race: African-American 50%, Latino-American 20%, White 15%, 10% Asian 5% Other
Religions: Christian 50%, 20% Catholic, 10% Mormon, 20% Other/None
Occupation: Local government 40%, Large corporation employee 20%, Small business employee 10%, Small business owner 10%, 20% Unemployed (high school, college)
Education: High School or equivalent 40%, College 30%, Some College 20%, Masters/Doctors 10%
Industry/Entity Type
Retail
Contact Information for Business Card
Name: Peter Olund
Title: Sales Associate
Address: 418 E. Mirabeth Ave. Gardena, CA 90247
Phone Number: 310.555.0182
Slogan: Broad Selection. Fair Prices, Friendly Service
www.granarycoatmart.example
Logo Text
GCM (Acronym for Granary Coat Mart) or Image
Requirements
Must have
- Easy to read
- Visually appealing

```html
<!DOCTYPE html>
<html lang="en">
<head>
<meta charset="utf-8">
<title>Granary Coat Mart – Business Card</title>
<link rel="stylesheet" href="https://fonts.googleapis.com/css2?family=Work+Sans:wght@400;500;600&display=swap">
<style>
  :root {
    --bg: #ecebea;
    --navy: #1f2230;
    --slate: #4a4d57;
    --silver: #b9bcc6;
    --paper: #ffffff;
    --red: #d9453a;
    --ink: #3c3e45;
  }
  * { margin: 0; padding: 0; box-sizing: border-box; }
  html, body { width: 1200px; height: 1000px; overflow: hidden; }
  body {
    background: var(--bg);
    font-family: "Work Sans", Arial, sans-serif;
    color: var(--ink);
    position: relative;
  }
  .card {
    position: absolute;
    top: 110px;
    width: 320px;
    height: 540px;
    box-shadow: 0 10px 30px rgba(0,0,0,0.12);
  }
  .card--front { left: 230px; background: var(--navy); }
  .card--back { left: 650px; background: var(--paper); }

  .brand-mark {
    display: flex; flex-direction: column; align-items: center; text-align: center;
  }
  .brand-mark__circle {
    border-radius: 50%;
    border-style: solid;
  }
  .card--front .brand-mark {
    position: absolute; left: 0; right: 0; top: 200px;
  }
  .card--front .brand-mark__circle {
    width: 66px; height: 66px; border-width: 3px; border-color: var(--silver);
  }
  .card--front .brand-mark__name {
    margin-top: 14px; font-size: 19px; font-weight: 500;
    letter-spacing: 2px; text-transform: uppercase; color: var(--silver);
  }

  .back__content {
    position: absolute; inset: 0; display: flex; flex-direction: column; align-items: center;
    padding-top: 44px;
  }
  .card--back .brand-mark__circle {
    width: 64px; height: 64px; border-width: 3px; border-color: var(--slate);
  }
  .person__name {
    margin-top: 24px; color: var(--red); font-size: 13px; font-weight: 500;
    letter-spacing: 7px; text-transform: uppercase;
  }
  .person__title {
    margin-top: 3px; font-size: 11px; letter-spacing: 3px; text-transform: uppercase;
  }
  .contact {
    margin-top: 38px; display: flex; flex-direction: column; align-items: center;
    font-size: 12px; letter-spacing: 1.5px;
  }
  .contact__icon { margin-bottom: 6px; }
  .contact__address { font-size: 11px; letter-spacing: 0.3px; }
  .contact + .contact { margin-top: 18px; }
  .slogan {
    margin-top: 32px; border: 1.5px solid var(--red); padding: 10px 14px;
    width: 244px; font-size: 11px; letter-spacing: 2px; line-height: 1.4;
    text-transform: uppercase;
  }
  .web { margin-top: 24px; display: flex; flex-direction: column; align-items: center; }
  .web__url { margin-top: 8px; font-size: 11px; letter-spacing: 2px; }

  .logo-lockup {
    position: absolute; left: 0; right: 0; top: 800px;
  }
  .logo-lockup .brand-mark__circle {
    width: 104px; height: 104px; border-width: 4px; border-color: var(--slate);
  }
  .logo-lockup .brand-mark__name {
    margin-top: 16px; font-size: 32px; font-weight: 500; letter-spacing: 3px;
    text-transform: uppercase; color: var(--slate);
  }
</style>
</head>
<body>
  <section class="card card--front">
    <div class="brand-mark">
      <div class="brand-mark__circle"></div>
      <div class="brand-mark__name">Granary Coat Mart</div>
    </div>
  </section>

  <section class="card card--back">
    <div class="back__content">
      <div class="brand-mark"><div class="brand-mark__circle"></div></div>
      <div class="person__name">Peter Olund</div>
      <div class="person__title">Sales Associate</div>

      <div class="contact">
        <svg class="contact__icon" width="14" height="20" viewBox="0 0 14 20">
          <rect x="2" y="1" width="10" height="18" rx="2" fill="none" stroke="var(--red)" stroke-width="1.5"/>
          <line x1="6" y1="16" x2="8" y2="16" stroke="var(--red)" stroke-width="1.5"/>
        </svg>
        <span>310.555.0182</span>
      </div>
      <div class="contact">
        <svg class="contact__icon" width="14" height="20" viewBox="0 0 14 20">
          <path d="M7 19 C3 13 1 10 1 7 A6 6 0 0 1 13 7 C13 10 11 13 7 19Z" fill="none" stroke="var(--red)" stroke-width="1.5"/>
          <circle cx="7" cy="7" r="2" fill="var(--red)"/>
        </svg>
        <span class="contact__address">418 E. Mirabeth Ave. Gardena, CA 90247</span>
      </div>

      <div class="slogan">Broad Selection.<br>Fair Prices,<br>Friendly Service</div>

      <div class="web">
        <svg width="12" height="16" viewBox="0 0 12 16">
          <path d="M1 1 L11 10 L6.5 10 L8.5 15 L6.5 15.8 L4.5 10.8 L1 13Z" fill="var(--red)"/>
        </svg>
        <span class="web__url">www.granarycoatmart.example</span>
      </div>
    </div>
  </section>

  <div class="logo-lockup brand-mark">
    <div class="brand-mark__circle"></div>
    <div class="brand-mark__name">Granary Coat Mart</div>
  </div>
</body>
</html>
```